orbit wellness loft
Project: logo for fitness studio
logo for fitness studio - Health
logo for fitness studio
Simple
Laura Whitfield
Certified Personal Trainer
482 W. Timber Ridge Rd. ElReno Ok. 73021
orbitwellness.owl@examplemail.test
I have already sent you most of my information .If you need more let me know .
Donna01 Donna01
I can't figure out how to change my brief. The email is wrong it's .owl@examplemail.test not .wol@examplemail.test so sorry. Also not so sure I like the black. The feeling I'm after is beach, sun and sand etc. thanks

```html
<!DOCTYPE html>
<html lang="en">
<head>
<meta charset="utf-8">
<title>orbit wellness loft — business cards</title>
<link rel="stylesheet" href="https://fonts.googleapis.com/css2?family=Montserrat:wght@300;400;600&display=swap">
<style>
  :root {
    --backdrop: #2b2b2d;
    --card-dark: #0b0b0c;
    --card-light: #ffffff;
    --teal: #2bb9bd;
    --silver: #b9bcc0;
    --ink: #4a4d52;
    --ink-soft: #8a8d92;
  }
  * { box-sizing: border-box; margin: 0; padding: 0; }
  html, body {
    width: 1200px; height: 754px; overflow: hidden;
    background: var(--backdrop);
    font-family: "Montserrat", sans-serif;
  }
  .stage { position: relative; width: 1200px; height: 754px; }
  .card {
    position: absolute; top: 222px;
    width: 540px; height: 310px; overflow: hidden;
    box-shadow: 0 14px 30px rgba(0,0,0,.45);
  }
  .card--front { left: 40px; background: var(--card-dark); }
  .card--back { left: 620px; background: var(--card-light); }

  .brand { display: flex; flex-direction: column; align-items: center; color: var(--teal); font-weight: 300; }
  .brand__dot { width: 54px; height: 54px; border: 2px solid var(--teal); border-radius: 50%; margin-bottom: 12px; }
  .brand__name { font-size: 30px; letter-spacing: 1px; line-height: 1.05; text-align: center; }

  .card--front .brand { position: absolute; left: 0; right: 0; top: 92px; }

  .card--back .brand { position: absolute; left: 30px; top: 70px; width: 230px; }
  .card--back .brand__name { font-size: 27px; }

  .contact { position: absolute; left: 300px; top: 40px; }
  .contact__name { font-size: 12px; font-weight: 600; color: var(--teal); letter-spacing: .5px; text-transform: uppercase; }
  .contact__role { font-size: 8px; color: var(--ink-soft); margin-top: 2px; margin-bottom: 14px; }
  .contact__list { list-style: none; }
  .contact__item { display: flex; align-items: center; gap: 8px; font-size: 8.5px; color: var(--ink); margin-bottom: 7px; }
  .contact__icon { width: 11px; height: 11px; flex: none; }

  .wave { position: absolute; left: 0; bottom: 0; width: 540px; height: 150px; }
  .address {
    position: absolute; left: 0; right: 0; bottom: 14px;
    text-align: center; font-size: 8px; color: #ffffff; letter-spacing: .3px;
  }
</style>
</head>
<body>
<main class="stage">
  <section class="card card--front" aria-label="Card front">
    <div class="brand">
      <span class="brand__dot"></span>
      <span class="brand__name">orbit wellness loft</span>
    </div>
  </section>

  <section class="card card--back" aria-label="Card back">
    <div class="brand">
      <span class="brand__dot"></span>
      <span class="brand__name">orbit wellness loft</span>
    </div>

    <div class="contact">
      <p class="contact__name">Laura Whitfield</p>
      <p class="contact__role">Personal Trainer</p>
      <ul class="contact__list">
        <li class="contact__item">
          <svg class="contact__icon" viewBox="0 0 12 12"><circle cx="6" cy="6" r="6" fill="var(--teal)"/><path d="M4 3.2l1 1.6-.6.6c.4.9 1.1 1.6 2 2l.6-.6 1.6 1-.5 1c-2.4-.2-4.4-2.2-4.6-4.6z" fill="#fff"/></svg>
          555 010 4821
        </li>
        <li class="contact__item">
          <svg class="contact__icon" viewBox="0 0 12 12"><circle cx="6" cy="6" r="6" fill="var(--teal)"/><rect x="4" y="2.6" width="4" height="6.8" rx=".8" fill="#fff"/></svg>
          555 010 4822
        </li>
        <li class="contact__item">
          <svg class="contact__icon" viewBox="0 0 12 12"><circle cx="6" cy="6" r="6" fill="var(--teal)"/><rect x="3" y="4.5" width="6" height="3.5" fill="#fff"/><rect x="4" y="3" width="4" height="1.5" fill="#fff"/></svg>
          555 010 4823
        </li>
        <li class="contact__item">
          <svg class="contact__icon" viewBox="0 0 12 12"><circle cx="6" cy="6" r="6" fill="var(--teal)"/><rect x="3" y="3.8" width="6" height="4.4" fill="#fff"/><path d="M3 3.8l3 2.4 3-2.4" stroke="var(--teal)" stroke-width=".7" fill="none"/></svg>
          orbitwellness.owl@examplemail.test
        </li>
        <li class="contact__item">
          <svg class="contact__icon" viewBox="0 0 12 12"><circle cx="6" cy="6" r="6" fill="var(--teal)"/><circle cx="6" cy="6" r="3" stroke="#fff" stroke-width=".8" fill="none"/><path d="M3 6h6M6 3v6" stroke="#fff" stroke-width=".6"/></svg>
          www.orbitwellnessloft.test
        </li>
      </ul>
    </div>

    <svg class="wave" viewBox="0 0 540 150" preserveAspectRatio="none" aria-hidden="true">
      <path d="M0 150 L0 112 C150 122 360 110 540 18 L540 150 Z" fill="var(--silver)"/>
      <path d="M0 150 L0 122 C160 128 370 118 540 38 L540 150 Z" fill="var(--teal)"/>
    </svg>
    <p class="address">482 W. Timber Ridge Rd. Fairhaven, ST 73021</p>
  </section>
</main>
</body>
</html>
```